Powerpoint design for european B2B business

We need a Powerpoint design for a newly established IT company with a B2B focus. We want to develop management information systems that help managers communicate goals into their organization and analyze their organizational activities and performance.

We defined the attached color scale, please relate your design to these colors.

The design should be simple and straight, serious and professional and leave enough space for the content ... :-)

Target Market(s)

B2B, companies larger than 200 employees

Industry/Entity Type

Business

Font styles to use
Sans Serif

Requirements
Should not have
• too playful design, clipart style

```html
<!DOCTYPE html>
<html lang="en">
<head>
<meta charset="utf-8">
<title>Veltrano – Presentation Template</title>
<link href="https://fonts.googleapis.com/css2?family=Oswald:wght@400;500;600&family=Open+Sans:wght@400;600;700&display=swap" rel="stylesheet">
<style>
  :root{
    --stage:#3a3a3a;
    --navy:#2d4b7b;
    --navy-dark:#1d355c;
    --navy-soft:#5a76a3;
    --green:#7c9a3c;
    --green-dark:#5f7d2a;
    --gold:#c9b036;
    --paper:#ffffff;
    --mist:#eef1f5;
    --line:#c9d1dc;
    --ink:#4a4f57;
    --photo-a:#8ea0b8;
    --photo-b:#4c5f7e;
  }
  *{box-sizing:border-box;margin:0;padding:0}
  html,body{width:863px;height:1200px;overflow:hidden;background:var(--stage)}
  body{position:relative;font-family:"Open Sans",Arial,sans-serif;color:var(--ink)}
  .slide{position:absolute;width:294px;height:218px;background:var(--paper);overflow:hidden}
  .col-l{left:140px}.col-r{left:452px}
  .row-1{top:150px}.row-2{top:392px}.row-3{top:634px}.row-4{top:876px}
  .abs{position:absolute}
  .photo{position:absolute;background:linear-gradient(135deg,var(--photo-a),var(--photo-b))}
  .photo.dark{background:linear-gradient(135deg,#3d5680,#1a2d4d)}
  .heading{font-family:"Oswald",Arial,sans-serif;font-weight:500;text-transform:uppercase;color:var(--navy);letter-spacing:.3px}
  .body{font-size:5.2px;line-height:1.55;color:var(--ink)}
  .white{color:#fff}
  .brand{font-family:"Open Sans",Arial,sans-serif;font-weight:600;color:var(--navy);font-size:26px;letter-spacing:-.5px}

  /* cover */
  .cover .brand-panel{left:96px;top:0;width:120px;height:218px;background:var(--paper);display:flex;align-items:center;justify-content:center}

  /* intro */
  .intro .card{right:14px;top:18px;width:120px;height:182px;background:var(--paper);padding:14px 12px}
  .intro .feature{display:flex;flex-direction:column;align-items:center;margin-bottom:14px}
  .intro .feature svg{margin-bottom:5px}
  .intro .lede{left:16px;top:22px;width:120px}

  /* team */
  .team .band{left:0;bottom:0;width:100%;height:78px;background:var(--navy)}
  .team .member{position:absolute;top:52px;width:70px;text-align:center}
  .team .avatar{width:48px;height:48px;border-radius:50%;margin:0 auto;border:3px solid var(--paper);background:linear-gradient(135deg,var(--photo-a),var(--photo-b))}
  .team .name{font-family:"Oswald",Arial,sans-serif;font-size:7px;margin-top:6px;color:var(--navy)}

  /* values */
  .values .tile{position:absolute;top:108px;width:78px;height:92px;background:var(--paper);text-align:center;padding:10px 6px}
  .values .tile svg{display:block;margin:0 auto 6px}

  /* steps */
  .steps .step{position:absolute;left:14px;width:150px;height:18px;background:var(--mist);display:flex;align-items:center}
  .steps .num{width:18px;height:18px;color:#fff;font-family:"Oswald",Arial,sans-serif;font-size:8px;display:flex;align-items:center;justify-content:center;margin-right:6px}

  /* services */
  .services .col{position:absolute;top:44px;width:112px}
  .services .col-head{height:14px;color:#fff;font-family:"Oswald",Arial,sans-serif;font-size:6.5px;display:flex;align-items:center;justify-content:center;text-transform:uppercase}
  .services .col-body{background:var(--mist);padding:8px;height:150px}
</style>
</head>
<body>

<!-- Cover -->
<section class="slide col-l row-1 cover">
  <div class="photo" style="left:0;top:0;width:294px;height:218px" role="img" aria-label="Photo of business people talking in an office"></div>
  <div class="abs brand-panel"><span class="brand">Veltrano</span></div>
</section>

<!-- Intro with feature card -->
<section class="slide col-r row-1 intro" style="background:var(--navy)">
  <div class="photo" style="left:0;top:0;width:294px;height:218px;opacity:.35" role="img" aria-label="Blue-toned office background photo"></div>
  <p class="abs lede body white" style="font-size:6px">Lorem ipsum dolor sit amet, consectetur adipiscing elit. Sed do eiusmod tempor incididunt ut labore et dolore magna aliqua. Ut enim ad minim veniam, quis nostrud exercitation ullamco laboris.</p>
  <div class="abs card">
    <div class="feature">
      <svg width="14" height="12" viewBox="0 0 14 12"><rect x="1" y="3" width="12" height="8" fill="var(--navy)"/><rect x="5" y="1" width="4" height="2" fill="none" stroke="var(--navy)"/></svg>
      <p class="body" style="text-align:center">Lorem ipsum dolor sit amet consectetur elit sed</p>
    </div>
    <div class="feature">
      <svg width="14" height="12" viewBox="0 0 14 12"><rect x="1" y="1" width="12" height="10" fill="none" stroke="var(--navy)" stroke-width="1.5"/><line x1="3" y1="5" x2="11" y2="5" stroke="var(--navy)"/><line x1="3" y1="8" x2="9" y2="8" stroke="var(--navy)"/></svg>
      <p class="body" style="text-align:center">Lorem ipsum dolor sit amet consectetur elit sed</p>
    </div>
    <div class="feature">
      <svg width="14" height="14" viewBox="0 0 14 14"><circle cx="5" cy="5" r="3.5" fill="var(--navy)"/><circle cx="10" cy="10" r="3" fill="none" stroke="var(--navy)" stroke-width="1.5"/></svg>
      <p class="body" style="text-align:center">Lorem ipsum dolor sit amet consectetur elit sed</p>
    </div>
  </div>
</section>

<!-- Image + text -->
<section class="slide col-l row-2">
  <div class="abs" style="left:10px;top:14px;width:120px;height:150px;background:var(--navy)"></div>
  <div class="photo" style="left:16px;top:20px;width:108px;height:138px" role="img" aria-label="Portrait photo of a business team"></div>
  <h2 class="abs heading" style="left:140px;top:16px;font-size:11px">Lorem ipsum dolor sit</h2>
  <p class="abs body" style="left:140px;top:36px;width:140px">Lorem ipsum dolor sit amet, consectetur adipiscing elit, sed do eiusmod tempor incididunt ut labore et dolore magna aliqua. Ut enim ad minim veniam, quis nostrud exercitation ullamco laboris nisi ut aliquip ex ea commodo consequat.</p>
  <div class="abs" style="left:0;bottom:0;width:100%;height:36px;background:var(--navy);display:flex;align-items:center;justify-content:center">
    <span class="heading white" style="font-size:9px;color:#fff">Lorem ipsum dolor sit</span>
  </div>
</section>

<!-- Team -->
<section class="slide col-r row-2 team">
  <h2 class="abs heading" style="left:0;width:100%;top:16px;text-align:center;font-size:12px">Out team members</h2>
  <div class="abs band"></div>
  <div class="member" style="left:38px"><div class="avatar" role="img" aria-label="Team member portrait"></div><div class="name white" style="color:#fff">LOREM IPSUM</div><p class="body white" style="color:#fff">Dolor sit amet</p></div>
  <div class="member" style="left:112px"><div class="avatar" role="img" aria-label="Team member portrait"></div><div class="name" style="color:#fff">LOREM IPSUM</div><p class="body" style="color:#fff">Dolor sit amet</p></div>
  <div class="member" style="left:186px"><div class="avatar" role="img" aria-label="Team member portrait"></div><div class="name" style="color:#fff">LOREM IPSUM</div><p class="body" style="color:#fff">Dolor sit amet</p></div>
</section>

<!-- Quality -->
<section class="slide col-l row-3">
  <div class="photo dark" style="left:0;top:0;width:294px;height:218px" role="img" aria-label="Dark blue photo of a modern office building"></div>
  <h2 class="abs heading" style="left:0;width:100%;top:14px;text-align:center;font-size:9px;color:#fff">Lorem ipsum dolor sit amet consectetur</h2>
  <div class="abs" style="left:40px;top:34px;width:214px;height:166px;background:var(--paper)">
    <div class="heading abs" style="left:96px;top:12px;font-size:14px;color:var(--gold)">Quality</div>
    <p class="abs body" style="left:96px;top:34px;width:108px">Lorem ipsum dolor sit amet, consectetur adipiscing elit sed do eiusmod.</p>
    <div class="photo" style="left:10px;top:70px;width:194px;height:88px" role="img" aria-label="Photo of colleagues meeting at a table"></div>
    <div class="photo" style="left:10px;top:10px;width:78px;height:54px" role="img" aria-label="Photo of a business meeting"></div>
  </div>
</section>

<!-- Values -->
<section class="slide col-r row-3 values" style="background:var(--mist)">
  <div class="photo" style="left:0;top:0;width:294px;height:120px;background:linear-gradient(135deg,#3f5d8d,#2a4470)" role="img" aria-label="Blue-tinted office photo"></div>
  <p class="abs white" style="left:18px;top:18px;width:250px;color:#fff;font-size:15px;line-height:1.25">Lorem ipsum dolor sit amet consectetur adipiscing elit.</p>
  <div class="tile" style="left:14px">
    <svg width="16" height="14" viewBox="0 0 16 14"><rect x="2" y="2" width="12" height="11" fill="var(--green)"/><rect x="5" y="5" width="2" height="2" fill="#fff"/><rect x="9" y="5" width="2" height="2" fill="#fff"/></svg>
    <p class="body">Lorem ipsum dolor sit amet, consectetur adipiscing elit sed do.</p>
  </div>
  <div class="tile" style="left:108px">
    <svg width="16" height="14" viewBox="0 0 16 14"><polygon points="8,1 15,5 1,5" fill="var(--green)"/><rect x="3" y="6" width="2" height="5" fill="var(--green)"/><rect x="7" y="6" width="2" height="5" fill="var(--green)"/><rect x="11" y="6" width="2" height="5" fill="var(--green)"/><rect x="1" y="12" width="14" height="2" fill="var(--green)"/></svg>
    <p class="body">Lorem ipsum dolor sit amet, consectetur adipiscing elit sed do.</p>
  </div>
  <div class="tile" style="left:202px">
    <svg width="16" height="14" viewBox="0 0 16 14"><path d="M1 3h5l2 2h7v8H1z" fill="var(--green)"/></svg>
    <p class="body">Lorem ipsum dolor sit amet, consectetur adipiscing elit sed do.</p>
  </div>
</section>

<!-- Steps -->
<section class="slide col-l row-4 steps">
  <h2 class="abs heading" style="left:0;width:100%;top:12px;text-align:center;font-size:12px">Lorem ipsum dolor sit amet</h2>
  <p class="abs body" style="left:0;width:100%;top:32px;text-align:center">Consectetur adipiscing elit</p>
  <div class="step" style="top:56px"><span class="num" style="background:var(--navy)">01</span><span class="body">Lorem ipsum dolor sit amet</span></div>
  <div class="step" style="top:80px"><span class="num" style="background:var(--green)">02</span><span class="body">Lorem ipsum dolor sit amet</span></div>
  <div class="step" style="top:104px"><span class="num" style="background:var(--navy)">03</span><span class="body">Lorem ipsum dolor sit amet</span></div>
  <div class="step" style="top:128px"><span class="num" style="background:var(--green)">04</span><span class="body">Lorem ipsum dolor sit amet</span></div>
  <div class="photo" style="left:172px;top:56px;width:108px;height:90px" role="img" aria-label="Photo of hands working at a laptop"></div>
  <div class="abs" style="left:0;bottom:0;width:100%;height:28px;background:var(--mist)"></div>
</section>

<!-- Services -->
<section class="slide col-r row-4 services">
  <h2 class="abs heading" style="left:0;width:100%;top:14px;text-align:center;font-size:10px">Our services</h2>
  <div class="col" style="left:26px">
    <div class="col-head" style="background:var(--green)">Lorem ipsum</div>
    <div class="col-body body">Lorem ipsum dolor sit amet, consectetur adipiscing elit, sed do eiusmod tempor incididunt ut labore et dolore magna aliqua. Ut enim ad minim veniam quis nostrud.</div>
  </div>
  <div class="col" style="left:156px">
    <div class="col-head" style="background:var(--navy)">Lorem ipsum</div>
    <div class="col-body body">Lorem ipsum dolor sit amet, consectetur adipiscing elit, sed do eiusmod tempor incididunt ut labore et dolore magna aliqua. Ut enim ad minim veniam quis nostrud.</div>
  </div>
</section>

</body>
</html>
```